Stationery Design Project

We need a stationery design for a consultancy called 'Marrow Ridge'. The design should communicate innovation and professionalism. The colors used should complement our logo. Please include source files for winning design.

Requirements
Must have
• Logo with company name should be included. Font of the text in logo should not be altered. Paper should be A4 sized and not Letter sized.

```html
<!DOCTYPE html>
<html lang="en">
<head>
<meta charset="utf-8">
<title>Marrow Ridge Stationery</title>
<link href="https://fonts.googleapis.com/css2?family=Cinzel:wght@500&family=Montserrat:wght@400;500;600&display=swap" rel="stylesheet">
<style>
  :root {
    --surface: #f3f3f3;
    --paper: #fdfdfd;
    --charcoal: #363535;
    --charcoal-deep: #2e2d2d;
    --amber: #e8952c;
    --gold: #e3a449;
    --ink: #555;
    --rule: #9a9a9a;
  }
  * { margin: 0; padding: 0; box-sizing: border-box; }
  html, body { width: 1200px; height: 979px; overflow: hidden; }
  body {
    position: relative;
    background: var(--surface);
    font-family: "Montserrat", sans-serif;
    color: var(--ink);
  }
  .piece { position: absolute; }
  .paper { background: var(--paper); }

  .brand {
    display: flex; flex-direction: column; align-items: center; justify-content: center;
    background: var(--charcoal);
  }
  .brand-dot { border-radius: 50%; background: var(--amber); }
  .brand-name {
    font-family: "Cinzel", serif; font-weight: 500;
    color: var(--gold); white-space: nowrap; letter-spacing: .3px;
  }

  /* Letterhead */
  .letterhead { left: 228px; top: 122px; width: 361px; height: 510px; }
  .letterhead .brand { position: absolute; left: 138px; top: 0; width: 83px; height: 83px; gap: 6px; }
  .letterhead .brand-dot { width: 36px; height: 36px; }
  .letterhead .brand-name { font-size: 9.5px; }
  .letterhead-footer { position: absolute; left: 38px; right: 40px; top: 464px; text-align: center; }
  .company-line { font-size: 8px; letter-spacing: .4px; color: #444; margin-left: 60px; }
  .footer-rule { height: 2px; background: var(--rule); margin: 5px 0 6px; }
  .contact-row { font-size: 5.2px; color: #555; display: flex; justify-content: center; gap: 8px; line-height: 8px; }

  /* Folder */
  .folder { left: 652px; top: 98px; width: 425px; height: 537px; background: var(--charcoal); }
  .folder .brand { position: absolute; left: 0; right: 0; top: 90px; background: none; gap: 8px; }
  .folder .brand-dot { width: 76px; height: 76px; }
  .folder .brand-name { font-size: 16px; }

  /* Business cards */
  .card { left: 98px; width: 163px; height: 92px; background: var(--charcoal-deep); }
  .card-front { top: 678px; }
  .card-front .brand { position: absolute; left: 0; top: 0; width: 84px; height: 92px; background: none; gap: 5px; }
  .card-front .brand-dot { width: 36px; height: 36px; }
  .card-front .brand-name { font-size: 9px; }
  .card-back { top: 796px; padding: 14px 12px; color: #ddd; }
  .person-name { font-size: 6.5px; font-weight: 600; letter-spacing: .4px; color: #fff; }
  .person-role { font-size: 5px; color: #ccc; margin-bottom: 10px; }
  .card-line { font-size: 4.2px; line-height: 6px; display: flex; align-items: center; gap: 3px; }
  .card-line i { width: 3.5px; height: 3.5px; border-radius: 50%; background: var(--amber); display: inline-block; }
  .card-address { font-size: 4.2px; line-height: 6px; margin-top: 4px; }

  /* Envelopes */
  .envelope-front { left: 303px; top: 691px; width: 404px; height: 193px; }
  .envelope-front .brand { position: absolute; left: 37px; top: 0; width: 84px; height: 85px; gap: 6px; }
  .envelope-front .brand-dot { width: 36px; height: 36px; }
  .envelope-front .brand-name { font-size: 9.5px; }
  .return-address { position: absolute; left: 51px; top: 163px; font-size: 5.4px; line-height: 8px; color: #555; }

  .envelope-back { left: 746px; top: 691px; width: 404px; height: 193px; }
  .envelope-flap { position: absolute; left: 0; top: 0; width: 100%; height: 68px; background: var(--charcoal); border-radius: 0 0 6px 6px; }
  .flap-seal { position: absolute; left: 194px; top: 26px; width: 17px; height: 17px; border-radius: 50%; background: var(--amber); }
</style>
</head>
<body>

  <section class="piece paper letterhead">
    <div class="brand">
      <span class="brand-dot"></span>
      <span class="brand-name">Marrow Ridge</span>
    </div>
    <footer class="letterhead-footer">
      <p class="company-line">MARROW RIDGE LLC</p>
      <div class="footer-rule"></div>
      <p class="contact-row"><span>4820 Lindell Ave. B-12, Austin, TX 78704</span><span>&#9742; 512-555-0143</span><span>&#9113; 512-555-0178</span></p>
      <p class="contact-row"><span>&#9993; hello@marrowridge.com</span><span>&#9711; www.marrowridge.com</span></p>
    </footer>
  </section>

  <section class="piece folder">
    <div class="brand">
      <span class="brand-dot"></span>
      <span class="brand-name">Marrow Ridge</span>
    </div>
  </section>

  <section class="piece card card-front">
    <div class="brand">
      <span class="brand-dot"></span>
      <span class="brand-name">Marrow Ridge</span>
    </div>
  </section>

  <section class="piece card card-back">
    <p class="person-name">DANIEL FOSTER</p>
    <p class="person-role">General Manager</p>
    <p class="card-line"><i></i>512-555-0143</p>
    <p class="card-line"><i></i>512-555-0178</p>
    <p class="card-line"><i></i>hello@marrowridge.com</p>
    <p class="card-line"><i></i>www.marrowridge.com</p>
    <p class="card-address">4820 Lindell Ave. B-12<br>Austin, TX 78704</p>
  </section>

  <section class="piece paper envelope-front">
    <div class="brand">
      <span class="brand-dot"></span>
      <span class="brand-name">Marrow Ridge</span>
    </div>
    <p class="return-address">4820 Lindell Ave. B-12<br>&nbsp;&nbsp;Austin, TX 78704</p>
  </section>

  <section class="piece paper envelope-back">
    <div class="envelope-flap"></div>
    <span class="flap-seal"></span>
  </section>

</body>
</html>
```